Website redesign

Looking to redesign our existing website. (quill7meadows.com.au)
New design needs to be bright, fun and have an easy flowing.
The website needs to be design with call to action.

Some examples of other websites:
fernquaylo.com
tovanmilk.com.au

We are happy with the content of our existing website.

Target Market(s)

other businesses

Industry/Entity Type

Business Service

Number of Pages Required

5+ page

Requirements
Must have
• Theme redesign
Cool animation similar to fernquaylo.com

```html
<!DOCTYPE html>
<html lang="en">
<head>
<meta charset="utf-8">
<title>Quill 7 Meadows – Virtual Assistants</title>
<link href="https://fonts.googleapis.com/css2?family=Montserrat:wght@500;600;700;800&family=Roboto:wght@400;500&display=swap" rel="stylesheet">
<style>
:root{
  --blue:#1f96e2;
  --ink:#151a22;
  --body:#3b4250;
  --pale:#e9eef5;
  --pale2:#eef1f6;
  --navy:#0e1a2c;
  --white:#ffffff;
}
*{box-sizing:border-box;margin:0;padding:0}
html,body{width:1200px;height:3974px;overflow:hidden}
body{font-family:"Roboto",Arial,sans-serif;color:var(--body);background:var(--white);position:relative}
section,header,footer{position:absolute;left:0;width:1200px}

/* header */
.site-header{top:0;height:102px;background:var(--white)}
.brand-name{position:absolute;left:173px;top:52px;color:var(--ink);font-family:"Montserrat",sans-serif;font-weight:600;font-size:19px;letter-spacing:-.2px;line-height:1}
.call{position:absolute;right:172px;top:18px;color:var(--blue);font-family:"Montserrat",sans-serif;font-weight:700;font-size:19px;display:flex;align-items:center;gap:8px}
.nav{position:absolute;top:64px;left:0;width:1200px;font-family:"Montserrat",sans-serif;font-weight:600;font-size:13px;color:var(--ink)}
.nav a{position:absolute;text-decoration:none;color:inherit}
.nav a.active{color:var(--blue)}

/* hero */
.hero{top:102px;height:536px;background:linear-gradient(120deg,#2a9fe8,#1b8fdc)}
.hero h1{position:absolute;left:173px;top:146px;color:var(--white);font-family:"Montserrat",sans-serif;font-weight:800;font-size:39px;line-height:40px}
.btn-dark{position:absolute;left:173px;top:293px;width:156px;height:42px;background:#10151f;color:var(--white);font-family:"Montserrat",sans-serif;font-weight:700;font-size:15px;display:flex;align-items:center;justify-content:center;box-shadow:4px 4px 0 var(--white)}
.hero-art{position:absolute;left:640px;top:75px;width:470px;height:380px;border-radius:14px;background:radial-gradient(circle at 55% 45%,rgba(255,255,255,.35),rgba(255,255,255,.08) 60%,transparent 75%)}

/* services */
.services{top:638px;height:542px}
.sec-title{position:absolute;left:0;width:1200px;text-align:center;font-family:"Montserrat",sans-serif;font-weight:700;color:var(--ink)}
.services .sec-title{top:70px;font-size:32px}
.services .lead{position:absolute;top:124px;left:400px;width:400px;text-align:center;font-size:13.5px;line-height:26px;color:var(--body)}
.svc{position:absolute;width:197px;height:216px;background:var(--white);box-shadow:0 4px 16px rgba(20,40,80,.1);text-align:center;padding-top:26px}
.svc svg{width:60px;height:66px}
.svc p{font-size:14px;line-height:21px;color:var(--body);margin:12px 16px 0}
.svc .bar{position:absolute;left:53px;bottom:24px;width:90px;height:4px;background:var(--blue)}

/* process */
.process{top:1180px;height:823px;background:var(--pale);overflow:hidden}
.process .sec-title{top:66px;font-size:33px}
.process svg.diagram{position:absolute;left:0;top:0}
.step-text{position:absolute;text-align:center;width:232px;transform:translateX(-50%)}
.step-text h3{font-family:"Montserrat",sans-serif;font-weight:700;font-size:16px;line-height:22px;color:var(--ink);margin-bottom:8px}
.step-text p{font-size:11.5px;line-height:15.5px;color:var(--body)}

/* outsourcing */
.outsource{top:2003px;height:796px}
.outsource h2{position:absolute;top:84px;left:0;width:1200px;text-align:center;font-family:"Montserrat",sans-serif;font-weight:700;font-size:26px;line-height:43px;color:var(--ink)}
.outsource .lead{position:absolute;top:178px;left:255px;width:690px;text-align:center;font-size:18px;line-height:29px;color:var(--body)}
.video{position:absolute;left:236px;top:295px;width:723px;height:404px;background:linear-gradient(100deg,#2a6fb0,#3d8ad0 45%,#2563a3)}
.video .play{position:absolute;left:336px;top:180px;width:52px;height:34px;border-radius:8px;background:#161616}
.video .play:after{content:"";position:absolute;left:21px;top:10px;border-left:13px solid #fff;border-top:7px solid transparent;border-bottom:7px solid transparent}
.video .controls{position:absolute;left:0;bottom:0;width:100%;height:26px;background:linear-gradient(transparent,rgba(0,0,0,.55))}

/* benefits */
.benefits{top:2799px;height:671px;background:var(--pale2)}
.benefits .sec-title{top:58px;font-size:34px}
.benefits .sub{position:absolute;top:112px;left:0;width:1200px;text-align:center;font-size:14px;color:var(--body)}
.ben{position:absolute;width:269px;height:205px;background:var(--white);box-shadow:0 3px 12px rgba(20,40,80,.08);text-align:center;padding-top:20px}
.ben svg{width:70px;height:70px}
.ben p{font-size:18px;line-height:23px;color:var(--body);margin-top:12px}

/* footer */
.site-footer{top:3470px;height:504px;background:var(--navy);color:var(--white)}
.foot-name{position:absolute;left:150px;top:130px;width:300px;text-align:center;font-family:"Montserrat",sans-serif;font-weight:600;font-size:23px;line-height:1}
.contacts{position:absolute;left:150px;top:192px;width:300px;text-align:center;font-size:13px;line-height:24px}
.contacts .m{color:var(--blue)}
.contacts .gap{height:24px}
.divider{position:absolute;left:517px;top:76px;width:1px;height:310px;background:#34425a}
.quote-title{position:absolute;left:578px;top:70px;font-family:"Montserrat",sans-serif;font-weight:600;font-size:24px}
.field{position:absolute;height:42px;border:1px solid #8b96a8;border-radius:3px;font-size:11px;padding:0 13px;display:flex;align-items:center;color:#dfe5ee}
.robot{position:absolute;left:580px;top:336px;width:244px;height:46px;border:1px solid #8b96a8;border-radius:3px;display:flex;align-items:center;gap:12px;padding-left:12px;font-size:10.5px}
.robot i{width:20px;height:20px;background:var(--white);border-radius:2px;display:inline-block}
.subscribe{position:absolute;left:845px;top:350px;display:flex;align-items:center;gap:8px;font-size:11px}
.subscribe i{width:15px;height:15px;border:1px solid #b8c1cf;display:inline-block}
.submit{position:absolute;left:578px;top:399px;width:119px;height:39px;background:var(--blue);font-family:"Montserrat",sans-serif;font-weight:700;font-size:16px;display:flex;align-items:center;justify-content:center;box-shadow:3px 3px 0 var(--white)}
.legal{position:absolute;left:173px;top:405px;font-size:13px;line-height:24px}
</style>
</head>
<body>

<header class="site-header">
  <div class="brand-name">QUILL 7 MEADOWS</div>
  <div class="call">
    <svg width="18" height="18" viewBox="0 0 24 24"><path fill="#1f96e2" d="M6.6 10.8a15.1 15.1 0 0 0 6.6 6.6l2.2-2.2c.3-.3.7-.4 1-.2 1.1.4 2.3.6 3.6.6.6 0 1 .4 1 1V20c0 .6-.4 1-1 1A17 17 0 0 1 3 4c0-.6.4-1 1-1h3.5c.6 0 1 .4 1 1 0 1.3.2 2.5.6 3.6.1.3 0 .7-.2 1z"/></svg>
    CALL US: 07 5550 1482
  </div>
  <nav class="nav">
    <a class="active" style="left:486px">HOME</a>
    <a style="left:572px">OUR STORY</a>
    <a style="left:697px">TIPS AND TRICKS</a>
    <a style="left:861px">CONTACT US</a>
    <a style="left:995px">FAQ</a>
  </nav>
</header>

<section class="hero">
  <h1>VIRTUAL ASSISTANT?<br>MORE LIKE<br>VALUABLE ASSET!</h1>
  <div class="btn-dark">CONTACT US</div>
  <div class="hero-art" role="img" aria-label="Isometric illustration of a large monitor with an infinity symbol, a person working on a laptop and support staff with floating chat icons"></div>
</section>

<section class="services">
  <h2 class="sec-title">OUR SERVICES</h2>
  <p class="lead">We'll help you save tens (or even hundreds!) of thousands of dollars per year. But what do WE actually do?</p>

  <div class="svc" style="left:173px;top:236px">
    <svg viewBox="0 0 60 66" fill="none" stroke="#1f96e2" stroke-width="2.4"><circle cx="30" cy="22" r="11"/><path d="M17 22a13 13 0 0 1 26 0"/><path d="M10 62c0-12 9-20 20-20s20 8 20 20"/><path d="M30 42v20"/></svg>
    <p>We recruit Virtual Assistants (a.k.a office legends!)</p>
  </div>
  <div class="svc" style="left:392px;top:213px">
    <svg viewBox="0 0 60 66" fill="none" stroke="#1f96e2" stroke-width="2.4"><circle cx="34" cy="20" r="13"/><circle cx="34" cy="20" r="5"/><path d="M6 50h10l12 6 20-8c3-1 3-5 0-6l-14 3H24"/><path d="M6 44h8v14H6z"/></svg>
    <p>Provide the tech support for these superheroes!</p>
    <span class="bar"></span>
  </div>
  <div class="svc" style="left:611px;top:236px">
    <svg viewBox="0 0 60 66" fill="none" stroke="#1f96e2" stroke-width="2.4"><rect x="16" y="4" width="28" height="52" rx="4"/><path d="M22 14h16M22 22h16M22 30h10"/><path d="M36 36l10 4v8c0 6-5 9-10 11-5-2-10-5-10-11v-8z"/></svg>
    <p>Set up the phone system (their own Bat Phone!)</p>
  </div>
  <div class="svc" style="left:830px;top:236px">
    <svg viewBox="0 0 60 66" fill="none" stroke="#1f96e2" stroke-width="2.4"><path d="M50 34a20 20 0 1 1-6-14"/><path d="M44 10v10h-10"/><circle cx="30" cy="34" r="12" fill="#1f96e2"/><text x="30" y="38" font-size="11" font-family="Arial" fill="#fff" stroke="none" text-anchor="middle">24</text></svg>
    <p>We manage Virtual Assistants and keep them in tip-top shape!</p>
  </div>
</section>

<section class="process">
  <h2 class="sec-title">THE PROCESS</h2>
  <svg class="diagram" width="1200" height="823" viewBox="0 0 1200 823">
    <defs>
      <radialGradient id="knob" cx="40%" cy="35%" r="70%"><stop offset="0" stop-color="#ffffff"/><stop offset="1" stop-color="#d4dbe4"/></radialGradient>
      <linearGradient id="hub" x1="0" y1="0" x2="0" y2="1"><stop offset="0" stop-color="#f3f5f8"/><stop offset="1" stop-color="#dfe4ea"/></linearGradient>
    </defs>
    <path d="M350 823 A250 250 0 0 1 850 823" fill="none" stroke="#10151f" stroke-width="3"/>
    <circle cx="600" cy="802" r="173" fill="url(#hub)" stroke="#c9d0da" stroke-width="3"/>
    <text x="600" y="760" text-anchor="middle" font-family="Montserrat, sans-serif" font-weight="700" font-size="22" fill="#151a22">QUILL 7 MEADOWS</text>
    <g fill="#fff" stroke="#1f96e2" stroke-width="4">
      <circle cx="378" cy="725" r="14"/><circle cx="464" cy="610" r="14"/><circle cx="600" cy="570" r="14"/><circle cx="736" cy="610" r="14"/><circle cx="822" cy="725" r="14"/>
    </g>
    <g fill="#10151f"><circle cx="378" cy="725" r="5"/><circle cx="464" cy="610" r="5"/><circle cx="600" cy="570" r="5"/><circle cx="736" cy="610" r="5"/><circle cx="822" cy="725" r="5"/></g>
    <g font-family="Montserrat, sans-serif" font-weight="700" font-size="17" fill="#151a22" text-anchor="middle">
      <g><path d="M300 740 L338 720 L322 700z" fill="#1f96e2"/><circle cx="265" cy="688" r="72" fill="#1f96e2"/><circle cx="265" cy="688" r="50" fill="url(#knob)"/><text x="265" y="694">STEP 1</text></g>
      <g><path d="M425 610 L448 600 L440 570z" fill="#1f96e2"/><circle cx="393" cy="510" r="72" fill="#1f96e2"/><circle cx="393" cy="510" r="50" fill="url(#knob)"/><text x="393" y="516">STEP 2</text></g>
      <g><path d="M590 510 L600 548 L615 510z" fill="#1f96e2"/><circle cx="600" cy="441" r="72" fill="#1f96e2"/><circle cx="600" cy="441" r="50" fill="url(#knob)"/><text x="600" y="447">STEP 3</text></g>
      <g><path d="M760 570 L752 600 L775 610z" fill="#1f96e2"/><circle cx="810" cy="510" r="72" fill="#1f96e2"/><circle cx="810" cy="510" r="50" fill="url(#knob)"/><text x="810" y="516">STEP 4</text></g>
      <g><path d="M878 700 L862 720 L900 740z" fill="#1f96e2"/><circle cx="938" cy="688" r="72" fill="#1f96e2"/><circle cx="938" cy="688" r="50" fill="url(#knob)"/><text x="938" y="694">STEP 5</text></g>
    </g>
  </svg>

  <div class="step-text" style="left:159px;top:442px">
    <h3>Provide Your<br>Preferred Qualifications.</h3>
    <p>Set up a call with our team to specify the requirements and qualifications you're searching for in a Virtual Assistant. This will be our checklist for your perfect assistant! From there, we'll take care of shortlisting, testing, background checking and recruiting.</p>
  </div>
  <div class="step-text" style="left:316px;top:236px">
    <h3>Endorsing the<br>Shortlisted Candidates</h3>
    <p>After the thorough vetting process, we'll put forward the best candidate. You can then conduct the final interview on your preferred communication platform at a time that suits you. Once the schedule is set, we'll let the candidates know!</p>
  </div>
  <div class="step-text" style="left:600px;top:168px">
    <h3>Conducting the<br>Final Interview</h3>
    <p>The final interview is the perfect time to get to know the candidates. It'll help to have a list of questions prepared that will help you pick out the chosen one!</p>
  </div>
  <div class="step-text" style="left:870px;top:259px">
    <h3>Setting up the Tools</h3>
    <p>Once you've chosen your Virtual Assistant, it's time for their system to be set up. You can get your own IT team onto the installation, otherwise, we've got a super team of tech peeps who can do it for you.</p>
  </div>
  <div class="step-text" style="left:1050px;top:404px">
    <h3>Your Magical<br>Journey Begins</h3>
    <p>Now you and your Virtual Assistant are all set up and ready to rumble! Feel the magic of having a reliable assistant to take on all the menial, repetitive, time-consuming tasks, and focus your energy on more important things. Meet new clients, explore business opportunities, or just spend some time with friends and family!</p>
  </div>
</section>

<section class="outsource">
  <h2>OUTSOURCING. A BIG WORD THAT<br>MEANS BIG THINGS FOR YOUR BUSINESS</h2>
  <p class="lead">Virtual Assistants are the superheroes of the modern office. They can do everything your team can do on a computer at a fraction of the price! (Well, maybe not high five you when you've had a win, but a virtual high five is definitely on the table!)</p>
  <div class="video" role="img" aria-label="Introductory video of the two company founders talking in front of a blue wall">
    <span class="play"></span>
    <span class="controls"></span>
  </div>
</section>

<section class="benefits">
  <h2 class="sec-title">IT'S TIME TO OUTSOURCE</h2>
  <p class="sub">Why are we your new best outsourcing friend?</p>

  <div class="ben" style="left:174px;top:156px">
    <svg viewBox="0 0 70 70" fill="none" stroke="#1f96e2" stroke-width="2.6"><circle cx="35" cy="16" r="7"/><path d="M24 38c0-7 5-12 11-12s11 5 11 12"/><path d="M6 30l8 18 12 6M64 30l-8 18-12 6"/></svg>
    <p>Your Own<br>Virtual Assistant</p>
  </div>
  <div class="ben" style="left:466px;top:156px">
    <svg viewBox="0 0 70 70" fill="none" stroke="#1f96e2" stroke-width="2.6"><rect x="12" y="6" width="38" height="54" rx="3"/><path d="M20 40V30M28 40V22M36 40V28"/><circle cx="48" cy="46" r="10"/><path d="M55 53l8 8"/></svg>
    <p>One Invoice<br>Per Month</p>
  </div>
  <div class="ben" style="left:757px;top:156px">
    <svg viewBox="0 0 70 70" fill="none" stroke="#1f96e2" stroke-width="2.6"><rect x="14" y="6" width="42" height="56" rx="3"/><path d="M20 16h30M20 40h30M28 52l14-8"/><text x="35" y="32" font-size="12" font-family="Arial" font-weight="700" fill="#1f96e2" stroke="none" text-anchor="middle">TAX</text></svg>
    <p>No Super or TAX</p>
  </div>
  <div class="ben" style="left:174px;top:381px">
    <svg viewBox="0 0 70 70" fill="none" stroke="#1f96e2" stroke-width="2.6"><rect x="12" y="14" width="46" height="42" rx="3" transform="rotate(-12 35 35)"/><path d="M22 46l10-10 8 6 12-14"/></svg>
    <p>Dedicated To Your<br>Business Only</p>
  </div>
  <div class="ben" style="left:466px;top:381px">
    <svg viewBox="0 0 70 70" fill="none" stroke="#1f96e2" stroke-width="2.6"><rect x="22" y="4" width="26" height="60" rx="4"/><path d="M30 10h10M32 56h6"/></svg>
    <p>Dedicated<br>Phone System</p>
  </div>
  <div class="ben" style="left:757px;top:381px">
    <svg viewBox="0 0 70 70" fill="none" stroke="#1f96e2" stroke-width="2.6"><path d="M14 38v-6a21 21 0 0 1 42 0v6"/><rect x="10" y="36" width="10" height="18" rx="3"/><rect x="50" y="36" width="10" height="18" rx="3"/><path d="M55 54c0 6-8 9-16 9"/></svg>
    <p>IT Setup and<br>Support</p>
  </div>
</section>

<footer class="site-footer">
  <div class="foot-name">QUILL 7 MEADOWS</div>
  <div class="contacts">
    <div>Ravi Tenner</div>
    <div class="m">Mobile: 0400 555 127</div>
    <div>Email: ravi@quill7meadows.com.au</div>
    <div class="gap"></div>
    <div>Mara Lindqvist</div>
    <div class="m">Mobile: 0400 555 864</div>
    <div>Email: mara@quill7meadows.com.au</div>
  </div>
  <div class="divider"></div>

  <div class="quote-title">GET A QUOTE</div>
  <div class="field" style="left:580px;top:120px;width:447px">Business Name</div>
  <div class="field" style="left:580px;top:174px;width:222px">Your First Name</div>
  <div class="field" style="left:813px;top:174px;width:214px">Your Surname</div>
  <div class="field" style="left:580px;top:227px;width:447px">Contact Number</div>
  <div class="field" style="left:580px;top:280px;width:447px">Email</div>
  <div class="robot"><i></i>I'm not a robot</div>
  <div class="subscribe"><i></i>Subscribe to our newsletter</div>
  <div class="submit">SUBMIT</div>

  <div class="legal">Virtual Assistant? More Like Valuable Asset!<br>© 2020 QUILL 7 MEADOWS | All rights reserved.</div>
</footer>

</body>
</html>
```